New Innovative Counselling and psychotherapy Service needs Business Card design

Keep it simple and professional. On one side, just company name and logo (perhaps in all blue) and maybe a tag line.

On other side (all white) my name and Qualifications in centre

Industry/Entity Type

Health And Wellness

Contact Information for Business Card

Derek Hollis
Counsellor & Psychotherapist
BSc (Psychol.), BA, Dip. (Couns. & Psych.), PG.Cert (CBT), ADLnR, ESGW

I will also require Mobile no, Email and web site address of which I'll pass on to final designer.

Font styles to use
Sans Serif

Requirements
Must have
• My Logo Only and please use the colours in logo that is in it.
Should not have
• Any other images

```html
<!DOCTYPE html>
<html lang="en">
<head>
<meta charset="utf-8">
<title>Kindred Lane – Business Card</title>
<link href="https://fonts.googleapis.com/css2?family=Open+Sans:ital,wght@0,300;0,400;0,600;0,700;1,400&display=swap" rel="stylesheet">
<style>
  :root {
    --backdrop: #3b3431;
    --card: #1a1b1d;
    --brand-blue: #3a9bd5;
    --brand-green: #7dbb42;
    --text-white: #f2f2f2;
    --text-grey: #8d8f93;
    --rule: #55575b;
  }
  * { margin: 0; padding: 0; box-sizing: border-box; }
  html, body {
    width: 1200px; height: 864px; overflow: hidden;
    background: var(--backdrop);
    font-family: "Open Sans", Arial, sans-serif;
  }
  .canvas { position: relative; width: 1200px; height: 864px; }
  .card {
    position: absolute; width: 525px; height: 300px;
    background: var(--card);
    box-shadow: 0 14px 30px rgba(0,0,0,.45);
  }
  .card--front { left: 55px; top: 130px; }
  .card--back { left: 620px; top: 420px; }

  .brand { position: absolute; display: flex; align-items: center; gap: 12px; }
  .brand__dot { width: 42px; height: 42px; border-radius: 50%; background: var(--brand-blue); }
  .brand__name { font-weight: 300; letter-spacing: -.5px; }

  .card--front .brand { left: 110px; top: 92px; }
  .card--front .brand__name { font-size: 40px; color: var(--text-grey); }
  .tagline {
    position: absolute; left: 0; right: 0; top: 200px; text-align: center;
    font-style: italic; font-size: 14px; color: var(--text-grey);
  }

  .card--back .brand { right: 30px; top: 60px; }
  .card--back .brand__dot { width: 32px; height: 32px; }
  .card--back .brand__name { font-size: 28px; color: var(--text-white); }

  .holder { position: absolute; left: 30px; top: 118px; }
  .holder__name { font-size: 17px; font-weight: 700; color: var(--brand-blue); text-transform: uppercase; }
  .holder__role { font-size: 14px; font-weight: 400; color: var(--brand-green); text-transform: uppercase; margin-top: 1px; }
  .holder__quals { font-size: 10.5px; color: var(--brand-green); line-height: 1.35; margin-top: 2px; }

  .contacts { position: absolute; left: 30px; top: 200px; list-style: none; }
  .contacts li { display: flex; align-items: center; gap: 9px; font-size: 13px; color: var(--text-white); line-height: 20px; }
  .contacts svg { width: 12px; height: 12px; fill: var(--brand-blue); flex: none; }

  .rule { position: absolute; left: 30px; right: 30px; top: 268px; height: 1px; background: var(--rule); }
</style>
</head>
<body>
<main class="canvas">
  <section class="card card--front">
    <div class="brand">
      <span class="brand__dot"></span>
      <span class="brand__name">Kindred Lane</span>
    </div>
    <p class="tagline">Caring For Your Psychological Well-Being Is Our Top Priority</p>
  </section>

  <section class="card card--back">
    <div class="brand">
      <span class="brand__dot"></span>
      <span class="brand__name">Kindred Lane</span>
    </div>
    <div class="holder">
      <h1 class="holder__name">Derek Hollis</h1>
      <h2 class="holder__role">Counsellor &amp; Psychotherapist</h2>
      <p class="holder__quals">BSc (Psychol.), BA, Dip. (Couns. &amp; Psych.)<br>PG.Cert (CBT), ADLnR, ESGW</p>
    </div>
    <ul class="contacts">
      <li>
        <svg viewBox="0 0 12 12" aria-hidden="true"><path d="M3 0h6a1 1 0 0 1 1 1v10a1 1 0 0 1-1 1H3a1 1 0 0 1-1-1V1a1 1 0 0 1 1-1zm0 1.5v8h6v-8z"/></svg>
        555 210 4478
      </li>
      <li>
        <svg viewBox="0 0 12 12" aria-hidden="true"><path d="M0 2h12v8H0z M1 3l5 3.5L11 3"/><path d="M1 3l5 3.5L11 3" stroke="#1a1b1d" stroke-width="1" fill="none"/></svg>
        derek@kindredlane.com
      </li>
      <li>
        <svg viewBox="0 0 12 12" aria-hidden="true"><circle cx="6" cy="6" r="6"/><path d="M1 6h10M6 0v12" stroke="#1a1b1d" stroke-width=".8"/></svg>
        www.kindredlane.com
      </li>
    </ul>
    <div class="rule"></div>
  </section>
</main>
</body>
</html>
```